Zielgruppe
Wir sind ein Restaurant und starten jetzt mit der Herstellung von eigenen Getränken wie z.B. Whisky, Gin, Rum, Weine, Liköre etc. Die erste Linie des Whiksy haben wir selbst entworfen möchten aber mehr Professionalität einbringen.
Aufgabenstellung
Beiliegend die beiden Flaschen welche bedruckt/beklebt werden (mit Flaschenbezeichnung) und unser LOGO als PSD.
Stichworte: Regional, Qualität, Beste Zutaten, keine Zusatzstoffe
Bezeichnungen: Silberfalter Whisky / Silberfalter Gin
Wichtig: Wiederkennungswert schaffen (Es sollen in Zukunft auch Weine, Liköre etc. produziert werden)
Infos Gin:
- 65 verschiedenen Botanicals
- Neben Blutorangen, Zitronen und Limetten, zeigt auch der Duft von Ingwer, Zitronengras und Kaffirlimettenblätter als Zitrusensemble das Facettenreichtum des Gins. Das Aromaspiel verändert sich nach etwas Zeit im Glas sehr deutlich. Dann zeigen sich starke Aromakomponenten wie Kardamom, Koriander oder Piment. Der Gin zeichnet sich aus durch seine Lebendigkeit
- 42%vol
- 500ml
Infos Whisky:
- 8 Jahre gereift
- Zur Vergärung unseres Whiskys verwenden wir eigens gezüchtete Frischhefe mit besonderen Fähigkeiten zur Bildung von sehr fruchtigen Gäraromen. Die Weichheit bekommt er durch die dreifache Destillation. Auch bei der Wahl unserer Gerste setzen wir auf unsere Region. Der Grund für diesen starken regionalen Bezug ist, dass wir versuchen unserem Whisky die größtmögliche Portion an Terroir zu verleihen. Bei der anschließenden Fasslagerung setzen wir auf hochwertige Fässer. Zuerst neue amerikanische Weißeiche mit anschließendem Sherry- und Cognacfass finish.
Tradition und Moderne verschmelzen zu einem unverwechselbaren Whisky, mit weichem, fruchtigen femininen Geschmack und wildem, maskulinen Charakter.
- Single Malt Whisky
- Geruch & Geschmack: Der Whisky zeichnet sich aus durch intensive, weiche Aromen nach Vanille und süßen Früchten, mit einem ungewöhnlich weichen und sanften Abgang mit einem Hauch von dunkler Schokolade.
Folgende obligatorischen Angaben sind Pflicht:
- Adresse 'Silberfalter / Lindenwiese 7 / 48213 Erlenbach-Mühlhausen'
- Losnummer z.B. L0121..

```html
<!DOCTYPE html>
<html lang="de">
<head>
<meta charset="utf-8">
<title>Silberfalter Whisky – Etikett</title>
<link rel="stylesheet" href="https://fonts.googleapis.com/css2?family=Archivo+Black&family=Open+Sans:wght@400;800&family=Vollkorn:wght@700&display=swap">
<style>
  :root {
    --gold: #fdbd5c;
    --ink: #000000;
    --paper: #ffffff;
  }
  html, body {
    margin: 0;
    padding: 0;
    overflow: hidden;
    background: #f2f2f2;
  }
  .label {
    position: relative;
    width: 1200px;
    height: 800px;
    box-sizing: border-box;
    border: 13px solid var(--gold);
    background: var(--ink);
    font-family: "Open Sans", sans-serif;
    overflow: hidden;
  }
  .label__artwork {
    position: absolute;
    left: 360px;
    top: 80px;
    width: 480px;
    height: 260px;
  }
  .label__brand {
    position: absolute;
    left: 0;
    right: 0;
    top: 340px;
    margin: 0;
    text-align: center;
    font-family: "Vollkorn", serif;
    font-weight: 700;
    font-size: 80px;
    line-height: 1;
    color: var(--gold);
    letter-spacing: 0.5px;
  }
  .label__spirit {
    position: absolute;
    left: 0;
    right: 0;
    top: 444px;
    margin: 0;
    text-align: center;
    font-family: "Archivo Black", sans-serif;
    font-size: 130px;
    line-height: 1;
    color: var(--gold);
    letter-spacing: -2px;
  }
  .label__age {
    position: absolute;
    left: 0;
    right: 0;
    top: 578px;
    margin: 0;
    text-align: center;
    font-weight: 800;
    font-size: 60px;
    line-height: 1;
    color: var(--gold);
  }
  .label__abv,
  .label__volume {
    position: absolute;
    top: 645px;
    margin: 0;
    font-weight: 400;
    font-size: 56px;
    line-height: 1;
    color: var(--paper);
  }
  .label__abv { left: 67px; letter-spacing: -1px; }
  .label__volume { right: 70px; }
  .label__claim {
    position: absolute;
    left: 0;
    right: 0;
    top: 665px;
    margin: 0;
    text-align: center;
    font-size: 20px;
    line-height: 1;
    color: var(--paper);
  }
  .label__address {
    position: absolute;
    left: 0;
    right: 0;
    top: 730px;
    margin: 0;
    text-align: center;
    font-size: 28px;
    line-height: 1;
    color: var(--paper);
    padding-right: 6px;
  }
</style>
</head>
<body>
  <main class="label">
    <svg class="label__artwork" viewBox="0 0 480 260" role="img" aria-label="Goldene Strichzeichnung einer auf einem Diwan liegenden Frau mit Zigarettenspitze">
      <rect width="480" height="260" fill="var(--gold)" opacity="0.55"/>
    </svg>
    <h1 class="label__brand">Silberfalter</h1>
    <p class="label__spirit">WHISKY</p>
    <p class="label__age">8 Jahre gereift</p>
    <p class="label__abv">42%vol</p>
    <p class="label__claim">Beste Qualität durch regionale Zutaten</p>
    <p class="label__volume">500 ml</p>
    <p class="label__address">Adresse 'Silberfalter / Lindenwiese 7 / 48213 Erlenbach-Mühlhausen'</p>
  </main>
</body>
</html>
```